Website Design for Korvelin.com.au (Design + Code)

I am a small business specialising in aquarium monitoring solutions.
Our products essentially are computerised monitoring equipment for aquariums. E.g. https://www.tidalmetrix.example/en-GB/products-shop/vantora-units
and also GloWard http://www.gloward.example/
I see the design having 3 pages
* Landing / Home
* Gallery
* Contact us
Design:
I am looking for a cutting edge slick looking site. It should have a number of pages so the site is interactive with contact us, gallery etc.
I have attached our logo and can provide more info as requested. I will be constantly changing the site content as well from my end.
I have attached my logo design which was done via MakerPlume. It can be changed/altered if you feel something else would work better
Final deliverable:
* This project requires both design and development (coding).
* The 3 design pages are to be delivered as PSD files, and the coding as HTML.
The site will need to scale to be viewable on both oSlate/otabs etc as well as standard desktop
Hi All,
Just based on the couple of designs that have come through so far I would like to specify that for the front landing page, I don't want to be product specific, but rather a page that describes the company and some information about what we do and why it is important to monitor your aquarium. It would still be good to have some images of the monitoring equipment, I will provide or modify the text with the information I am talking about above.
I hope this a little more specific.
Hi All,
While I like the designs that are coming through, I still feel that they are all very template based in look and feel.
I am looking for a unique design that is interactive and engaging to the viewer.
If you need more information from me, please let me know.
Please feel free to submit completely new designs.
Kind Regards,
Tarvesh

```html
<!DOCTYPE html>
<html lang="nl">
<head>
<meta charset="utf-8">
<title>Korvelin – Aquarium Monitoring</title>
<link href="https://fonts.googleapis.com/css2?family=Arimo:wght@400;700&display=swap" rel="stylesheet">
<style>
  :root {
    --navy: #1e4263;
    --page-grey: #f2f2f2;
    --white: #ffffff;
    --ink: #222222;
    --body-ink: #333333;
    --accent: #23a3dc;
    --accent-dark: #1a86b8;
    --nav-top: #2a2a2a;
    --nav-bottom: #000000;
    --enquiry: #58585c;
    --line-light: rgba(255,255,255,0.25);
    --sea-top: #1233c4;
    --sea-deep: #0b2aa8;
    --reef: #4a3a86;
  }
  * { box-sizing: border-box; margin: 0; padding: 0; }
  html, body { width: 1200px; height: 895px; overflow: hidden; }
  body {
    font-family: "Arimo", Helvetica, Arial, sans-serif;
    background: linear-gradient(to bottom, var(--navy) 0, var(--navy) 507px, var(--page-grey) 507px);
    position: relative;
  }
  .site {
    position: absolute; left: 154px; top: 45px; width: 877px; height: 850px;
    background: var(--white); border-top: 5px solid var(--accent);
  }
  .phone {
    position: absolute; right: 29px; top: 15px;
    display: flex; align-items: center; gap: 6px;
    font-size: 18px; font-weight: 700; color: #4a4a4a; letter-spacing: -0.3px;
  }
  .main-nav {
    position: absolute; left: 0; top: 60px; width: 100%; height: 40px;
    background: linear-gradient(to bottom, var(--nav-top), var(--nav-bottom));
  }
  .main-nav ul { list-style: none; position: absolute; right: 30px; top: 12px; display: flex; gap: 18px; }
  .main-nav a { color: var(--white); text-decoration: none; font-weight: 700; font-size: 13.5px; letter-spacing: -0.2px; }
  .brand {
    position: absolute; left: 30px; top: 0; width: 235px; height: 110px;
    background: var(--white); display: flex; align-items: flex-end; justify-content: center;
    padding-bottom: 20px; gap: 10px; text-decoration: none;
  }
  .brand-mark { width: 14px; height: 14px; background: var(--accent); margin-bottom: 6px; }
  .brand-name { font-size: 32px; font-weight: 400; color: #555555; letter-spacing: -0.5px; line-height: 1; }
  .hero {
    position: absolute; left: 0; top: 100px; width: 100%; height: 297px;
    background:
      linear-gradient(to top, rgba(74,58,134,0.55) 0, rgba(74,58,134,0) 90px),
      linear-gradient(to bottom, var(--sea-top), var(--sea-deep));
  }
  .card { position: absolute; top: 338px; width: 253px; height: 230px; }
  .card-title {
    height: 60px; display: flex; align-items: center; justify-content: center;
    font-size: 17px; font-weight: 700; text-transform: uppercase; letter-spacing: -0.4px;
  }
  .news { left: 30px; background: var(--accent); color: var(--white); }
  .news .card-title { border-bottom: 1px solid var(--line-light); }
  .news ul { list-style: none; margin: 8px 22px 0; }
  .news li {
    display: flex; align-items: center; gap: 8px; height: 41px;
    font-size: 12px; border-bottom: 1px solid var(--line-light); letter-spacing: -0.1px;
  }
  .news-icon { width: 11px; height: 11px; border: 1.5px solid var(--white); position: relative; flex: none; }
  .news-icon::after { content: ""; position: absolute; left: 2px; top: 2px; width: 3px; height: 3px; background: var(--white); }
  .products { left: 313px; background: var(--white); border: 1px solid #e2e2e2; color: var(--ink); }
  .products .card-title { border-bottom: 1px solid #e6e6e6; }
  .product-shot {
    position: absolute; left: 73px; top: 86px; width: 94px; height: 116px; border-radius: 6px;
    background: linear-gradient(135deg, #3c3c3c, #1c1c1c);
    border-right: 5px solid #2a5fd0;
  }
  .arrow { position: absolute; top: 133px; }
  .arrow.prev { left: 22px; }
  .arrow.next { right: 22px; }
  .enquiry { left: 595px; background: var(--enquiry); color: var(--white); }
  .enquiry .card-title { border-bottom: 1px solid var(--line-light); }
  .enquiry p { text-align: center; font-size: 12px; margin-top: 20px; }
  .field {
    position: absolute; background: var(--white); height: 28px; border: 1px solid #dddddd;
    font-size: 12px; color: #444444; padding: 7px 6px;
  }
  .send {
    position: absolute; left: 76px; top: 178px; width: 98px; height: 28px;
    background: linear-gradient(to bottom, #2fb0e8, var(--accent-dark));
    color: var(--white); font-size: 12px; font-weight: 700;
    display: flex; align-items: center; justify-content: center; border: 1px solid #167aa8;
  }
  .section-title {
    position: absolute; left: 0; width: 100%; text-align: center;
    font-size: 17px; font-weight: 700; color: var(--ink); text-transform: uppercase; letter-spacing: -0.5px;
  }
  .section-title span { display: inline-block; padding-bottom: 10px; border-bottom: 4px solid var(--accent); }
  .about-title { top: 630px; }
  .about-text {
    position: absolute; left: 0; top: 692px; width: 877px; text-align: center;
    font-size: 11.5px; line-height: 18px; color: var(--body-ink); white-space: nowrap; letter-spacing: -0.1px;
  }
  .about-text p + p { margin-top: 18px; }
  .services-title { top: 818px; }
</style>
</head>
<body>
  <div class="site">
    <header>
      <div class="phone">
        <svg width="30" height="30" viewBox="0 0 30 30" aria-hidden="true">
          <circle cx="15" cy="15" r="13.5" fill="none" stroke="#23a3dc" stroke-width="2"/>
          <path d="M10.5 8.5c1-.8 2-.6 2.5.3l1.2 2.3c.4.8.2 1.5-.5 2l-.9.7c.6 1.8 2 3.4 3.8 4.3l.8-.9c.6-.6 1.3-.7 2-.3l2.2 1.4c.8.5.9 1.5.2 2.4-1.2 1.5-3 1.8-5 .8-3.4-1.7-6-4.6-7.2-8.2-.6-1.9-.3-3.6.9-4.8z" fill="#23a3dc"/>
        </svg>
        <span>0100 - 55 21 07</span>
      </div>
      <nav class="main-nav">
        <ul>
          <li><a href="#">HOME</a></li>
          <li><a href="#">ABOUT</a></li>
          <li><a href="#">WEBSHOP</a></li>
          <li><a href="#">CONTACT</a></li>
        </ul>
      </nav>
      <a class="brand" href="#">
        <span class="brand-mark"></span>
        <span class="brand-name">Korvelin</span>
      </a>
    </header>

    <div class="hero" role="img" aria-label="Underwater photo of tropical reef fish swimming over coral"></div>

    <section class="card news">
      <h2 class="card-title">Latest News</h2>
      <ul>
        <li><span class="news-icon"></span>Persbericht campagne Voeten in</li>
        <li><span class="news-icon"></span>Stafbureau gesloten op vrijdag 10</li>
        <li><span class="news-icon"></span>Waarom kiezen voor een VitaPas</li>
      </ul>
    </section>

    <section class="card products">
      <h2 class="card-title">Newest Products</h2>
      <svg class="arrow prev" width="22" height="34" viewBox="0 0 22 34" aria-hidden="true">
        <path d="M18 3L5 17l13 14" fill="none" stroke="#555555" stroke-width="6"/>
      </svg>
      <div class="product-shot" role="img" aria-label="Product photo of an aquarium monitoring controller unit"></div>
      <svg class="arrow next" width="22" height="34" viewBox="0 0 22 34" aria-hidden="true">
        <path d="M4 3l13 14L4 31" fill="none" stroke="#23a3dc" stroke-width="6"/>
      </svg>
    </section>

    <section class="card enquiry">
      <h2 class="card-title">Enquiry</h2>
      <p>Lipsum is diola eboalega seva heva.</p>
      <div class="field" style="left:22px; top:105px; width:100px;">Name</div>
      <div class="field" style="left:130px; top:105px; width:100px;">Email</div>
      <div class="field" style="left:22px; top:141px; width:208px;">Message</div>
      <div class="send">Send</div>
    </section>

    <h2 class="section-title about-title"><span>About Korvelin Aquarium Monitoring</span></h2>
    <div class="about-text">
      <p>Mijn naam is Marit Veldkamp en ik ben 25 jaar oud. Vanaf februari 2012 ben ik begonnen aan de opleiding voor pedicure, deze opleiding volg ik bij<br>Lindeboom-opleidingen in Rotterdam.</p>
      <p>het is nu mei en ik ben geslaagd voor mijn laatste theorie examen!! vanaf 20 mei kan ik opgeroepen worden voor het praktijk examen dus dat schiet ook al op.<br>ik heb het afgelopen jaar erg veel geleerd en er valt nog veel meer te leren in dit vak, wat ik ook zeker wil blijven doen.</p>
    </div>

    <h2 class="section-title services-title"><span>What We Do</span></h2>
  </div>
</body>
</html>
```